Mortgage Broking Flyer to attract attention

We are looking for double sided, colour DL sized flyers for a mail drop to inform people what services we offer.
We are a Mortgage Broking Business in Alice Springs NT Australia. Alice Springs is a large country town so we want something that is personal, a little bit playful but still professional, and is going to capture the attention of potential clients when they first look at it so they want to read on.
Please use our logo and colours (red & white) plus a photo of our team – all attached.
Brochure Front: IMPORTANT
Please come up with a tag line based on the following-We want to be seen as different to the bank, more friendly, personable, we listen, want to help and want people to keep coming back even for the little things.
The home page from our website has good dot points but we would like them shorter and to the point www.ochrepeakfinance.com.au
Plus include something which lets customer know that we can assist purchases made through any real estate office, anywhere in Australia
Don’t want the front to contain too many long sentences or paragraphs.
Brochure Back:
Please include:
Services/Specialties
• First home buyers
• Refinancing
• Investments
• Construction loans
• Debt consolidation
• Commercial finance
Please include the following contact details:
Dominic Wexley – Managing Director
Marisol Fenwicke – Loans Consultant
Tamsin Pallister – Loans Consultant
Suite 4/17 Gundry Street, Alice Springs NT 0870
Phone: 08 8927 4158
www.ochrepeakfinance.com.au
We must include the following fine print at the back/bottom of the brochure:
Dominic Wexley (Credit Representative Number: 512873), Marisol Fenwicke (Credit Representative Number: 512874) and Tamsin Pallister (Credit Representative Number: 637215) are credit representatives of QVTRO Pty Ltd (Australian Credit Licence Number: 748016)
Please feel free to email me with any questions.
kerry@ochrepeakfinance.com.au

```html
<!DOCTYPE html>
<html lang="en">
<head>
<meta charset="utf-8">
<title>Ochre Peak Finance – DL Flyer</title>
<link href="https://fonts.googleapis.com/css2?family=Cabin:ital,wght@0,400;0,500;0,600;1,500;1,700&family=Oswald:wght@500;600&family=Roboto+Condensed:wght@300;400&family=Arimo:ital,wght@1,400&display=swap" rel="stylesheet">
<style>
  :root{
    --red:#d3202e;
    --red-dark:#a8121d;
    --pink:#fde7e9;
    --ink:#141414;
    --grey:#2b2b2b;
    --white:#ffffff;
    --stage:#e8e6e3;
  }
  *{margin:0;padding:0;box-sizing:border-box}
  html,body{width:1200px;height:958px;overflow:hidden;background:var(--stage)}
  .canvas{position:relative;width:1200px;height:958px;background:var(--stage)}
  .panel{position:absolute;top:39px;width:442px;height:880px;background:var(--white);overflow:hidden;box-shadow:0 4px 14px rgba(0,0,0,.18)}
  .panel--front{left:130px}
  .panel--back{left:628px}
  .panel svg.bands{position:absolute;left:0;top:0;width:442px;height:880px}
  .abs{position:absolute}
  .center{left:0;right:0;text-align:center}

  .brand{position:absolute;top:44px;left:0;right:0;display:flex;align-items:center;justify-content:center;gap:14px}
  .brand__dot{width:46px;height:46px;border-radius:50%;background:var(--red)}
  .brand__name{font-family:"Roboto Condensed",sans-serif;font-weight:300;font-size:34px;letter-spacing:.5px;color:var(--ink);text-transform:uppercase}

  /* front */
  .hero-photo{position:absolute;left:88px;top:131px;width:268px;height:268px;border-radius:50%;
    background:radial-gradient(circle at 35% 40%,#eef1f4 0%,#c9d2da 45%,#6f7a85 100%)}
  .tagline{top:432px;font-family:Cabin,sans-serif;color:var(--ink)}
  .tagline__lead{font-size:32px;font-weight:500;line-height:34px}
  .tagline__accent{font-size:28px;font-weight:600;color:var(--red);line-height:32px}
  .tagline__sub{font-size:20px;font-weight:500;line-height:26px}
  .tagline__rule{width:360px;height:2px;background:var(--red);margin:4px auto 0}
  .welcome{top:540px;font-family:Oswald,sans-serif;font-weight:500;font-size:31px;color:var(--ink);letter-spacing:-.5px}
  .offer{left:36px;top:598px;font-family:Cabin,sans-serif;font-style:italic;font-weight:700;font-size:21px;color:var(--red)}
  .offer-list{position:absolute;left:36px;right:46px;top:632px;list-style:none;font-family:Cabin,sans-serif;font-size:13.8px;color:var(--grey);line-height:15px}
  .offer-list li{position:relative;padding-left:16px;margin-bottom:9px}
  .offer-list li::before{content:"";position:absolute;left:0;top:4px;width:7px;height:7px;border-radius:50%;background:var(--red)}
  .web{font-family:Cabin,sans-serif;font-style:italic;font-weight:700;font-size:18px;color:var(--white)}
  .panel--front .web{top:822px}

  /* back */
  .team-photo{position:absolute;left:0;top:96px;width:442px;height:240px;
    background:linear-gradient(180deg,#7e8f5e 0%,#a7b487 45%,#d9c6b2 80%,#e9e2da 100%)}
  .services-title{left:44px;top:343px;font-family:Arimo,sans-serif;font-style:italic;font-size:20px;color:var(--ink);letter-spacing:.3px}
  .services-title span{color:var(--red)}
  .services{position:absolute;top:381px;list-style:none;font-family:Cabin,sans-serif;font-weight:500;font-size:17.5px;color:var(--white);line-height:24px}
  .services li::before{content:"\2022";margin-right:4px}
  .services--a{left:44px}
  .services--b{left:234px}
  .fineprint{position:absolute;left:44px;right:22px;top:476px;list-style:none;font-family:Cabin,sans-serif;font-size:12.6px;color:var(--ink);line-height:15.5px}
  .fineprint li{position:relative;padding-left:13px;margin-bottom:3px}
  .fineprint li::before{content:"";position:absolute;left:0;top:6px;width:4px;height:4px;border-radius:50%;background:var(--red)}
  .team{position:absolute;left:40px;top:606px;width:186px;font-family:Cabin,sans-serif;text-align:center}
  .team__member{height:46px;padding-top:3px}
  .team__name{font-size:18.5px;font-weight:500;color:var(--ink);line-height:19px}
  .team__role{font-size:15.5px;font-weight:500;color:var(--red);line-height:17px}
  .call{left:256px;top:640px;font-family:Oswald,sans-serif}
  .call__label{font-size:25px;font-weight:600;color:var(--ink);line-height:30px}
  .call__phone{font-size:29px;font-weight:500;color:var(--red);line-height:36px;letter-spacing:-.3px}
  .address{top:802px;font-family:Cabin,sans-serif;font-style:italic;font-weight:500;font-size:13.5px;color:var(--white)}
  .panel--back .web{top:822px;font-size:20px}
</style>
</head>
<body>
<div class="canvas">

  <!-- Front -->
  <section class="panel panel--front">
    <svg class="bands" viewBox="0 0 442 880" aria-hidden="true">
      <defs>
        <linearGradient id="redFront" x1="0" y1="0" x2="0" y2="1">
          <stop offset="0" stop-color="#e2323d"/><stop offset="1" stop-color="#b5141f"/>
        </linearGradient>
      </defs>
      <rect x="0" y="150" width="442" height="300" fill="url(#redFront)"/>
      <polygon points="0,0 442,0 442,150 222,190 0,150" fill="#fff"/>
      <polyline points="0,140 222,180 442,140" fill="none" stroke="#111" stroke-width="2"/>
      <polygon points="0,240 210,282 0,300" fill="#fff"/>
      <polygon points="442,240 232,282 442,300" fill="#fff"/>
      <polygon points="0,418 222,380 442,418 442,880 0,880" fill="#fff"/>
      <polyline points="0,428 222,390 442,428" fill="none" stroke="#111" stroke-width="2"/>
      <circle cx="222" cy="265" r="146" fill="#fff" stroke="#d3202e" stroke-width="2"/>
      <polygon points="0,800 222,788 442,800 442,880 0,880" fill="url(#redFront)"/>
    </svg>

    <div class="brand"><span class="brand__dot"></span><span class="brand__name">Ochre Peak Finance</span></div>
    <div class="hero-photo" role="img" aria-label="Photo of a smiling businesswoman on the phone with colleagues shaking hands behind her"></div>

    <div class="abs center tagline">
      <p class="tagline__lead">Big or Less thing,</p>
      <p class="tagline__accent">come to us to experience</p>
      <p class="tagline__sub">a friendly and personalized service</p>
      <div class="tagline__rule"></div>
    </div>
    <h1 class="abs center welcome">Welcome to Ochre Peak Finance</h1>
    <p class="abs offer">Ochre Peak Finance offer:</p>
    <ul class="offer-list">
      <li>Local staff, local business assisting with their local knowledge</li>
      <li>We proactively manage the whole lending process for you</li>
      <li>Residential, Investment and Commercial Lending</li>
      <li>We do the hard work for you</li>
      <li>All the flexibility you need</li>
      <li>We are paid by the bank at no extra cost to you</li>
    </ul>
    <p class="abs center web">www.ochrepeakfinance.com</p>
  </section>

  <!-- Back -->
  <section class="panel panel--back">
    <div class="team-photo" role="img" aria-label="Team photo of the three loan staff standing in front of a large gum tree"></div>
    <svg class="bands" viewBox="0 0 442 880" aria-hidden="true">
      <defs>
        <linearGradient id="redBack" x1="0" y1="0" x2="0" y2="1">
          <stop offset="0" stop-color="#c81a26"/><stop offset="1" stop-color="#a8121d"/>
        </linearGradient>
      </defs>
      <polygon points="0,0 442,0 442,96 222,172 0,96" fill="#fff"/>
      <polygon points="0,92 222,170 442,92 442,104 222,184 0,104" fill="#d3202e"/>
      <rect x="0" y="334" width="442" height="8" fill="#c81a26"/>
      <rect x="0" y="342" width="442" height="32" fill="#fde7e9"/>
      <rect x="0" y="374" width="442" height="90" fill="url(#redBack)"/>
      <rect x="0" y="464" width="442" height="114" fill="#fde7e9"/>
      <rect x="0" y="578" width="442" height="16" fill="#b5141f"/>
      <line x1="215" y1="604" x2="442" y2="604" stroke="#111" stroke-width="2"/>
      <line x1="215" y1="712" x2="442" y2="758" stroke="#111" stroke-width="2"/>
      <polygon points="0,770 200,752 442,786 442,880 0,880" fill="url(#redBack)"/>
      <circle cx="133" cy="680" r="109" fill="#fff" stroke="#d3202e" stroke-width="1.5"/>
      <circle cx="133" cy="680" r="101" fill="#d3202e"/>
      <circle cx="133" cy="680" r="95" fill="#fde7e9"/>
      <line x1="45" y1="654" x2="221" y2="654" stroke="#111" stroke-width="1.5"/>
      <line x1="45" y1="700" x2="221" y2="700" stroke="#111" stroke-width="1.5"/>
    </svg>

    <div class="brand"><span class="brand__dot"></span><span class="brand__name">Ochre Peak Finance</span></div>

    <h2 class="abs services-title">SERVICES <span>/</span> SPECIALTIES :</h2>
    <ul class="services services--a">
      <li>First home buyers</li>
      <li>Refinancing</li>
      <li>Investments</li>
    </ul>
    <ul class="services services--b">
      <li>Construction loans</li>
      <li>Debt consolidation</li>
      <li>Commercial finance</li>
    </ul>
    <ul class="fineprint">
      <li>Dominic Wexley (Credit Representative Number: 512873)</li>
      <li>Marisol Fenwicke (Credit Representative Number: 512874)</li>
      <li>Tamsin Pallister (Credit Representative Number: 637215)</li>
      <li>are credit representatives of QVTRO Pty Ltd (Australian Credit Licence Number: 748016)</li>
    </ul>

    <div class="team">
      <div class="team__member"><p class="team__name">Dominic Wexley</p><p class="team__role">Managing Director</p></div>
      <div class="team__member"><p class="team__name">Marisol Fenwicke</p><p class="team__role">Loans Consultant</p></div>
      <div class="team__member"><p class="team__name">Tamsin Pallister</p><p class="team__role">Loans Consultant</p></div>
    </div>

    <div class="abs call">
      <p class="call__label">CALL US NOW:</p>
      <p class="call__phone">08 8927 4158</p>
    </div>

    <p class="abs center address">ADDRESS: Suite 4/17 Gundry Street, Alice Springs NT 0870</p>
    <p class="abs center web">www.ochrepeakfinance.com</p>
  </section>

</div>
</body>
</html>
```